Pelling Home Efficiency

Id like for my business card to be very bold and professional. Incorporating the business logo, the main services offered, and my contact info. Services are spray foam, insulation, new construction, retrofit, weatherization.

When opening this project art huddle was not able to upload my new logo that I picked from another recent art huddle project. Does anyone know how i could upload my logo onto the page for design of the business cards?

Target Market(s)

Building owners, contractors

Industry/Entity Type

Building Insulation and performance improvements

Contact Information for Business Card

Owner, Email marcus@pellinghomeefficiency.com Phone number 555-204-6817

Colors
0054AA
0677BA
7BADD7
CADEEF
E8F1F8
F0912C
F2A743
F7CA91
FBE8D2
FDF5EE

Requirements
Must have
• Services- spray foam, cellulose, mineral wool, fiberglass, air sealing, new construction, retrofit, weatherization, energy saving assesments

```html
<!DOCTYPE html>
<html lang="en">
<head>
<meta charset="utf-8">
<title>Pelling Home Efficiency – Business Card</title>
<link rel="stylesheet" href="https://fonts.googleapis.com/css2?family=Montserrat:wght@400;500;600;800&display=swap">
<style>
  :root {
    --stage: #2a2a2c;
    --sky: #3db3e3;
    --orange: #f08a3a;
    --orange-text: #f07a1c;
    --white: #ffffff;
    --ink: #2a2a2a;
  }
  * { box-sizing: border-box; margin: 0; padding: 0; }
  html, body { width: 1200px; height: 875px; overflow: hidden; }
  body {
    background: var(--stage);
    font-family: "Montserrat", Arial, sans-serif;
    position: relative;
  }
  .card {
    position: absolute;
    width: 540px;
    height: 310px;
    border-radius: 18px;
    overflow: hidden;
    box-shadow: 0 18px 40px rgba(0,0,0,.45);
  }
  /* Front: services */
  .card-front { left: 40px; top: 282px; background: var(--sky); color: var(--white); }
  .brand {
    position: absolute; left: 0; right: 0; top: 62px;
    display: flex; align-items: center; justify-content: center; gap: 14px;
  }
  .brand-mark { width: 26px; height: 26px; background: currentColor; flex: none; }
  .brand-name { font-weight: 800; font-size: 30px; letter-spacing: .5px; text-transform: uppercase; line-height: 1.1; }
  .services-title {
    position: absolute; left: 0; right: 0; top: 150px; text-align: center;
    font-weight: 600; font-size: 22px;
  }
  .services-title span { border-bottom: 2px solid var(--white); padding-bottom: 2px; }
  .services-list {
    position: absolute; left: 40px; right: 40px; top: 200px; text-align: center;
    font-weight: 600; font-size: 14.5px; line-height: 1.45;
  }

  /* Back: contact */
  .card-back { left: 620px; top: 282px; background: var(--white); }
  .card-back .bands { position: absolute; inset: 0; }
  .back-brand {
    position: absolute; left: 34px; top: 100px; width: 225px;
    display: flex; align-items: center; gap: 10px; color: var(--orange-text);
  }
  .back-brand .brand-mark { width: 20px; height: 20px; }
  .back-brand .brand-name { font-size: 19px; }
  .divider { position: absolute; left: 276px; top: 54px; width: 2px; height: 120px; background: var(--orange); }
  .contact { position: absolute; left: 296px; top: 50px; right: 16px; color: var(--ink); }
  .person-name { font-weight: 800; font-size: 23px; color: var(--orange-text); line-height: 1.2; }
  .person-role { font-weight: 500; font-size: 13px; margin-bottom: 10px; }
  .contact-row { display: flex; align-items: center; gap: 8px; font-size: 13px; line-height: 1.6; }
  .contact-row svg { width: 13px; height: 13px; fill: var(--sky); flex: none; }
  .address {
    position: absolute; left: 0; width: 330px; top: 218px; text-align: center;
    color: var(--white); font-size: 14px; font-weight: 500;
  }
</style>
</head>
<body>
  <section class="card card-front">
    <div class="brand">
      <span class="brand-mark"></span>
      <span class="brand-name">Pelling Home Efficiency</span>
    </div>
    <h2 class="services-title"><span>Services</span></h2>
    <p class="services-list">spray foam, cellulose, mineral wool, fiberglass, air sealing, new construction, retrofit, weatherization, energy saving assesments</p>
  </section>

  <section class="card card-back">
    <svg class="bands" viewBox="0 0 540 310" preserveAspectRatio="none" aria-hidden="true">
      <polygon points="0,205 350,205 330,250 0,250" fill="var(--sky)"/>
      <polygon points="362,205 540,205 540,250 342,250" fill="var(--orange)"/>
    </svg>
    <div class="back-brand">
      <span class="brand-mark"></span>
      <span class="brand-name">Pelling Home Efficiency</span>
    </div>
    <div class="divider"></div>
    <div class="contact">
      <div class="person-name">Dana Whitfield</div>
      <div class="person-role">Managing Director</div>
      <div class="contact-row">
        <svg viewBox="0 0 16 16"><path d="M3 1l3 3-2 2c1 2 3 4 6 6l2-2 3 3-2 2C7 15 1 9 1 3z"/></svg>
        <span>(08) 5550 1842</span>
      </div>
      <div class="contact-row">
        <svg viewBox="0 0 16 16"><path d="M1 3h14v10H1z M1 3l7 6 7-6" fill="none" stroke="var(--sky)" stroke-width="1.8"/></svg>
        <span>info@pellinghome.net</span>
      </div>
      <div class="contact-row">
        <svg viewBox="0 0 16 16"><circle cx="8" cy="8" r="7"/></svg>
        <span>www.pellinghome.net</span>
      </div>
    </div>
    <div class="address">48 Alder Lane, Brookfield, USA</div>
  </section>
</body>
</html>
```